Bref créative
Meridel Beauty Supply
Brochure
Kept the prize money low as all I want to do is duplicate our web site with minor changes to create the brochure. Web address is www.meridelbeautysupply.example
Salons and hairstylists
The site was built by brandcraftnook.example so I am hoping that the imagery, text etc will be available to the designer.

```html
<!DOCTYPE html>
<html lang="en">
<head>
<meta charset="utf-8">
<title>Meridel Beauty Supply – Brochure</title>
<link href="https://fonts.googleapis.com/css2?family=Arimo:wght@400;700&family=Parisienne&display=swap" rel="stylesheet">
<style>
  :root {
    --magenta: #a3175a;
    --magenta-dark: #7e0f44;
    --ink: #3a3a3a;
    --paper: #ffffff;
    --tile-dark: #141414;
    --rule: #e6d3dc;
  }
  * { margin: 0; padding: 0; box-sizing: border-box; }
  html, body { width: 1200px; height: 929px; overflow: hidden; background: var(--paper); }
  .brochure { position: relative; width: 1200px; height: 929px; font-family: "Arimo", Arial, sans-serif; color: var(--ink); overflow: hidden; }
  .backdrop { position: absolute; inset: 0; }
  .panel { position: absolute; top: 0; height: 929px; }
  .panel--products { left: 0; width: 397px; }
  .panel--local { left: 397px; width: 401px; }
  .panel--cover { left: 798px; width: 402px; }

  .section-title { position: absolute; font-family: "Parisienne", cursive; font-weight: 400; }
  .products-title { left: 38px; top: 14px; font-size: 30px; color: var(--paper); }
  .product-list { position: absolute; left: 14px; top: 68px; list-style: none; }
  .product-list li { font-size: 15px; line-height: 34px; padding-left: 26px; position: relative; }
  .product-list li::before, .local-list li::before {
    content: ""; position: absolute; left: 4px; top: 50%; width: 0; height: 0;
    border-left: 11px solid var(--magenta); border-top: 5px solid transparent; border-bottom: 5px solid transparent;
    transform: translateY(-50%) rotate(-20deg);
  }

  .brand-grid { position: absolute; left: 30px; top: 560px; display: grid; grid-template-columns: 163px 163px; column-gap: 8px; row-gap: 12px; }
  .brand-tile { height: 50px; display: flex; align-items: center; justify-content: center; font-size: 17px; font-weight: 700; background: var(--paper); color: var(--magenta); }
  .brand-tile--dark { background: var(--tile-dark); color: var(--paper); }

  .local-title { left: 52px; top: 120px; font-size: 34px; color: var(--magenta); }
  .local-list { position: absolute; left: 34px; top: 178px; width: 340px; list-style: none; }
  .local-list li { font-size: 15px; line-height: 21px; padding-left: 26px; margin-bottom: 14px; position: relative; }
  .local-list li::before { top: 10px; }

  .city-photo { position: absolute; left: 43px; top: 488px; width: 326px; height: 192px; border: 6px solid var(--paper);
    background: linear-gradient(180deg, #6fa6d8 0%, #9cc3e6 38%, #c9b89b 52%, #3f76a8 62%, #2d5f8c 100%); }
  .contact { position: absolute; left: 0; top: 802px; width: 401px; text-align: center; color: var(--paper); font-size: 15px; line-height: 20px; }

  .logo { position: absolute; left: 40px; top: 270px; width: 330px; text-align: right; color: var(--magenta); }
  .logo-mark { display: inline-block; width: 16px; height: 16px; background: var(--magenta); margin-bottom: 8px; }
  .logo-name { display: block; font-size: 56px; line-height: 58px; font-weight: 400; }
  .logo-sub { display: block; font-size: 22px; font-weight: 400; letter-spacing: 1px; }

  .tagline { position: absolute; left: 60px; top: 552px; width: 330px; text-align: center; font-family: "Parisienne", cursive; font-size: 27px; line-height: 36px; color: var(--paper); }
  .spa-photo { position: absolute; left: 0; top: 640px; width: 402px; height: 289px;
    background: linear-gradient(100deg, var(--magenta) 0%, #c25a6e 30%, #e2b08f 60%, #f1cdb0 80%, #7a2448 100%); }
</style>
</head>
<body>
<main class="brochure">
  <svg class="backdrop" width="1200" height="929" viewBox="0 0 1200 929" aria-hidden="true">
    <!-- products panel: corner banner and lower band -->
    <path d="M0 0 H190 L150 30 L118 56 L0 62 Z" fill="var(--magenta)"/>
    <path d="M0 70 L22 40 L30 72 Z" fill="var(--magenta)"/>
    <path d="M0 548 Q200 528 397 540 V929 H0 Z" fill="var(--magenta)"/>
    <!-- local panel: top points and lower band -->
    <path d="M397 0 H798 V30 L720 70 L700 20 L640 55 L560 0 L520 80 L470 20 L430 60 Z" fill="var(--magenta)"/>
    <path d="M397 455 Q600 430 798 470 V929 H397 Z" fill="var(--magenta)"/>
    <!-- cover panel: lower band -->
    <path d="M798 548 Q1000 520 1200 535 V929 H798 Z" fill="var(--magenta)"/>
    <line x1="397" y1="0" x2="397" y2="929" stroke="var(--rule)" stroke-width="1"/>
    <line x1="798" y1="0" x2="798" y2="929" stroke="var(--rule)" stroke-width="1"/>
  </svg>

  <section class="panel panel--products">
    <h2 class="section-title products-title">Products</h2>
    <ul class="product-list">
      <li>Verda – Natural Botanical Category</li>
      <li>Curlsome – Curly Category</li>
      <li>Luxeon – Luxury/Color Care Category</li>
      <li>Greenleaf Organics – Organic Category</li>
      <li>Harbor Crew – Men’s Category</li>
      <li>Stylo – Styling Edgy Category</li>
      <li>Quirkette – Eccentric Category</li>
      <li>Keldon – Hair Color Category</li>
      <li>Nailora – Professional Nail Category</li>
      <li>Polira – Nail Color Category</li>
      <li>Ironline – Styling Appliance Category</li>
      <li>Marisol – Brush – Brushes</li>
      <li>Bladewell – Shears</li>
      <li>Blossa – Cosmetics</li>
    </ul>
    <div class="brand-grid">
      <div class="brand-tile">Verda</div>
      <div class="brand-tile">Greenleaf</div>
      <div class="brand-tile">Luxeon</div>
      <div class="brand-tile">Avonlea Tools</div>
      <div class="brand-tile">Polira</div>
      <div class="brand-tile">Curlsome</div>
      <div class="brand-tile brand-tile--dark">Quirkette</div>
      <div class="brand-tile brand-tile--dark">Keldon</div>
      <div class="brand-tile brand-tile--dark">Harbor Crew</div>
      <div class="brand-tile">Oakmere Brush</div>
      <div class="brand-tile brand-tile--dark">Stylo</div>
      <div class="brand-tile brand-tile--dark">Ironline</div>
    </div>
  </section>

  <section class="panel panel--local">
    <h2 class="section-title local-title">Keeping it Local</h2>
    <ul class="local-list">
      <li>San Diego owned and operated</li>
      <li>Over 30 years experience in the San Diego salon market</li>
      <li>A non-corporate, boutique distributor focused on local salon professionals.</li>
      <li>We offer a beautiful, centrally located salon educational facility making education convenient for our clients</li>
      <li>Local, efficient and affordable shipping</li>
    </ul>
    <div class="city-photo" role="img" aria-label="Photo of a waterfront city skyline across a bay"></div>
    <address class="contact">
      Office: (555)014-7775<br>
      Toll free at (888)555-0146<br>
      Dana Whitlock: (555)019-4569<br>
      Email: info@meridelbeautysupply.example<br>
      Web: www.meridelbeautysupply.example
    </address>
  </section>

  <section class="panel panel--cover">
    <div class="logo">
      <span class="logo-mark"></span>
      <span class="logo-name">Meridel</span>
      <span class="logo-sub">beauty supply</span>
    </div>
    <p class="tagline">Bringing Personalized Services<br>Back to the Salon</p>
    <div class="spa-photo" role="img" aria-label="Photo of a client relaxing during a salon head massage with pink flowers"></div>
  </section>
</main>
</body>
</html>
```